Website Landing Page for Brightfall Systems

Create a custom designed website landing page for our business. Looking for a professional upscale design that incorporates our logo and logo colors into the theme. I want a standard fixed frame website, not a constant scrolling format that seems to be the trend. To start with I'm looking for more of the graphic design part, maybe a concept or theme, I don't expect to see a finished project. Not interested in generic templates or layouts.

The name of our company is Brightfall Systems and I've attached our logo below. I'd like to have the web page have the same look and feel of our logo, as well as the colors. Our company, Brightfall Systems does system design, installation, and programming, of residential and commercial Audio/Video and Automation systems. We do home theaters, lighting and building automation, video conferencing systems, security camera installations, conference rooms, projectors, distributed audio systems, and similar Technology projects. This will be a professional services/informational website. We will not sell products on this website. This website will be used to advertise our company and communicate our services to prospective customers. Having a well designed, professional and clean website is one way we want to distinguish our company from the competition.

Here are some examples of what I consider a professional well designed website
http://www.qorlamstudio.com/Work/

Last year we had our tradlo store designed (with PixelMarket) and I'm really happy with the way it turned out. You can see it at www.HolvenGearDepot.com I consider this to be a great design and looking for the same level of quality with this new website. However, do not copy or use any part of this design in this new project. This tradlo store is completely separate from our other company Brightfall Systems. I only mention this tradlo store an an example of good work.

Reason: Still going through designs.

Reason: Still working on project and have not had time to review all designs and request revisions.

Reason: Sill going through designs and requesting revisions

Reason: still going through all the submissions we received.

Target Market(s)

People interested in Audio/Video, home theaters, home automation. We do sales, system design, and programming. We typically work on larger projects with both residential and commercial customers.

Industry/Entity Type

Business

Number of Pages Required

1 page

Requirements
Must have
• Great design elements. Please use a white background. I think white goes well with our logo colors.

```html
<!DOCTYPE html>
<html lang="en">
<head>
<meta charset="utf-8">
<title>Brightfall Systems</title>
<link href="https://fonts.googleapis.com/css2?family=Lato:wght@400;700&family=Montserrat:wght@600&display=swap" rel="stylesheet">
<style>
:root{
  --navy:#0c0f2c;
  --navy-2:#141a45;
  --footer:#0b0e30;
  --green:#5aac44;
  --blue:#3d8fd6;
  --light:#e2e2e2;
  --team-bg:#ebebeb;
  --text-dark:#333;
  --text-body:#555;
  --white:#fff;
}
*{margin:0;padding:0;box-sizing:border-box}
html,body{width:1200px;height:3158px;overflow:hidden}
body{position:relative;font-family:'Lato',sans-serif;background:var(--white);color:var(--text-dark)}
.section{position:absolute;left:0;width:1200px;overflow:hidden}
.abs{position:absolute}

/* hero */
.hero{top:0;height:674px;background:var(--navy)}
.hero-photo{position:absolute;inset:0;background:
  radial-gradient(ellipse 90px 120px at 960px 420px,rgba(40,120,130,.55),transparent 80%),
  radial-gradient(ellipse 260px 120px at 930px 220px,rgba(150,120,95,.55),transparent 75%),
  radial-gradient(ellipse 420px 330px at 900px 340px,#4a4541 0%,#2b2a31 45%,transparent 85%),
  radial-gradient(ellipse 320px 90px at 300px 470px,rgba(60,66,90,.5),transparent 80%),
  linear-gradient(180deg,#11142f 0%,#0c0e27 55%,#080a1c 100%)}
.hero-shade{position:absolute;inset:0;background:linear-gradient(90deg,rgba(8,10,30,.75) 0%,rgba(8,10,30,.35) 45%,rgba(8,10,30,0) 70%)}
.brand{left:124px;top:26px;display:flex;align-items:center;gap:12px}
.brand-mark{width:54px;height:54px;border:4px solid var(--blue);border-radius:50%}
.brand-name{color:var(--green);font-weight:700;font-size:15px;line-height:17px;letter-spacing:1px;text-transform:uppercase;width:110px}
.nav{left:598px;top:44px;display:flex;gap:40px}
.nav a{color:var(--white);text-decoration:none;font-size:16px;text-transform:uppercase;padding-bottom:8px}
.nav a.active{border-bottom:3px solid var(--green)}
.hero-title{left:122px;top:280px;font-family:'Montserrat',sans-serif;font-weight:600;font-size:36px;color:var(--blue);letter-spacing:.5px}
.hero-title span{color:var(--green)}
.hero-text{left:124px;top:330px;width:450px;color:var(--white);font-weight:700;font-size:14px;line-height:17px}
.btn{background:var(--green);color:var(--white);font-weight:700;font-size:14px;text-transform:uppercase;display:flex;align-items:center;justify-content:center}
.hero-btn{left:124px;top:402px;width:164px;height:40px}
.dots{left:551px;top:598px;display:flex;gap:16px}
.dots i{width:22px;height:22px;border-radius:50%;background:#2a2f4c}
.dots i.on{background:var(--blue)}

/* section heads */
.title{left:0;width:1200px;text-align:center;font-size:21px;font-weight:700;text-transform:uppercase;letter-spacing:.5px}
.lead{left:124px;width:952px;text-align:center;font-size:14px;line-height:18px}

/* about */
.about{top:674px;height:690px;background:var(--light)}
.about .title{top:55px;color:var(--text-dark)}
.about .lead{top:130px;color:var(--text-body)}
.about-photos{left:0;top:225px}

/* services */
.services{top:1364px;height:575px;background:var(--navy)}
.services-photo{position:absolute;inset:0;background:
  linear-gradient(180deg,rgba(12,15,44,.55),rgba(12,15,44,.9) 60%),
  radial-gradient(ellipse 500px 160px at 300px 250px,#2c3350,transparent 80%),
  radial-gradient(ellipse 500px 200px at 900px 300px,#262c48,transparent 80%),
  linear-gradient(90deg,#1f2440,#141834 50%,#1c2140)}
.services .title{top:46px;color:var(--white)}
.services .lead{top:116px;color:var(--white)}
.service{top:242px;width:300px;text-align:center;color:var(--white)}
.service svg{display:block;margin:0 auto}
.service h3{font-size:16px;font-weight:700;margin-top:20px}
.service p{font-size:13px;line-height:17px;margin:14px auto 0;width:250px}

/* team */
.team{top:1939px;height:657px;background:var(--team-bg)}
.team .title{top:48px;color:var(--text-dark)}
.member{top:128px;width:297px;height:406px;background:var(--green);color:var(--white)}
.member-photo{height:261px}
.member h3{font-size:18px;font-weight:700;margin:20px 20px 0}
.member .role{font-size:13px;font-weight:700;text-transform:uppercase;margin:12px 20px 0}
.member p{font-size:13px;line-height:16px;margin:10px 20px 0}

/* contact */
.contact{top:2596px;height:562px;background:var(--navy-2)}
.contact-photo{position:absolute;inset:0;background:
  radial-gradient(ellipse 420px 230px at 560px 310px,#262d58,transparent 80%),
  linear-gradient(180deg,#16194a,#121642 70%,#0f1238)}
.footer-band{position:absolute;left:0;top:478px;width:1200px;height:84px;background:var(--footer)}
.contact .title{top:46px;color:var(--white)}
.field{height:42px;border:2px solid var(--green);color:var(--white);font-size:13px;text-transform:uppercase;padding:12px 14px}
.send{left:519px;top:385px;width:162px;height:46px;font-size:15px}
.footer-note{right:124px;top:514px;color:var(--white);font-size:15px}
</style>
</head>
<body>

<header class="section hero">
  <div class="hero-photo" role="img" aria-label="Modern house at dusk with lit terrace beside a lake"></div>
  <div class="hero-shade"></div>
  <div class="abs brand"><span class="brand-mark"></span><span class="brand-name">Brightfall Systems</span></div>
  <nav class="abs nav">
    <a class="active" href="#">Home</a><a href="#">About Us</a><a href="#">Services</a><a href="#">Team</a><a href="#">Contact</a>
  </nav>
  <h1 class="abs hero-title">BEST DEAL.<span>BEST SERVICES</span></h1>
  <p class="abs hero-text">Lorem ipsum dolor sit amet, consectetur adipiscing elit, sed do eiusmod tempor incididunt ut labore et dolore magna aliqua. Ut enim ad minim.</p>
  <div class="abs btn hero-btn">Read More</div>
  <div class="abs dots"><i class="on"></i><i></i><i></i></div>
</header>

<section class="section about">
  <h2 class="abs title">About Us</h2>
  <p class="abs lead">Lorem ipsum dolor sit amet, consectetur adipiscing elit, sed do eiusmod tempor incididunt ut labore et dolore magna aliqua. Ut enim ad minim veniam, quis nostrud exercitation ullamco laboris nisi ut aliquip ex ea commodo consequat. Duis aute irure dolor in reprehenderit in voluptate velit esse cillum dolore eu fugiat nulla pariatur.</p>
  <svg class="abs about-photos" width="1200" height="465" viewBox="0 0 1200 465">
    <defs>
      <linearGradient id="villaModern" x1="0" y1="0" x2="0" y2="1">
        <stop offset="0" stop-color="#cfdbe8"/><stop offset=".2" stop-color="#eef1f4"/><stop offset=".45" stop-color="#c6c8ca"/><stop offset=".62" stop-color="#6f6b66"/><stop offset=".78" stop-color="#4a5a60"/><stop offset="1" stop-color="#3a3733"/>
      </linearGradient>
      <linearGradient id="villaClassic" x1="0" y1="0" x2="0" y2="1">
        <stop offset="0" stop-color="#2457d6"/><stop offset=".3" stop-color="#3f63c2"/><stop offset=".45" stop-color="#e8e2cf"/><stop offset=".65" stop-color="#d9b86a"/><stop offset=".8" stop-color="#4f5a48"/><stop offset="1" stop-color="#7a7e8c"/>
      </linearGradient>
    </defs>
    <path role="img" aria-label="Modern white villa with pool and deck" d="M0 8 Q250 -12 420 60 Q600 200 760 465 L0 465 Z" fill="url(#villaModern)"/>
    <path role="img" aria-label="Classic villa lit at night with palm trees" d="M747 465 Q650 300 610 195 Q800 10 1200 2 L1200 465 Z" fill="url(#villaClassic)"/>
  </svg>
</section>

<section class="section services">
  <div class="services-photo" role="img" aria-label="City skyline at night"></div>
  <h2 class="abs title">Services</h2>
  <p class="abs lead">Lorem ipsum dolor sit amet, consectetur adipiscing elit, sed do eiusmod tempor incididunt ut labore et dolore magna aliqua. Ut enim ad minim veniam, quis nostrud exercitation ullamco laboris nisi ut aliquip ex ea commodo consequat. Duis aute irure dolor in reprehenderit in voluptate velit esse cillum dolore eu fugiat nulla pariatur.</p>

  <div class="abs service" style="left:115px">
    <svg width="134" height="134" viewBox="0 0 134 134">
      <circle cx="67" cy="67" r="65" fill="var(--blue)"/>
      <g fill="none" stroke="#fff" stroke-width="5" stroke-linejoin="round">
        <path d="M40 52 L88 40 L95 62 L47 74 Z"/>
        <path d="M62 72 L68 86 L80 86"/>
        <path d="M30 80 L30 96 M30 88 L62 88"/>
      </g>
      <circle cx="86" cy="55" r="4" fill="#fff"/>
    </svg>
    <h3>Lorem Ipsum</h3>
    <p>Lorem ipsum dolor sit amet, consectetur adipiscing elit, sed do eiusmod tempor incididunt ut labore et dolore.</p>
  </div>

  <div class="abs service" style="left:450px">
    <svg width="134" height="134" viewBox="0 0 134 134">
      <circle cx="67" cy="67" r="63" fill="none" stroke="var(--blue)" stroke-width="3"/>
      <g fill="none" stroke="var(--blue)" stroke-width="4" stroke-linejoin="round">
        <path d="M36 66 L67 38 L98 66"/>
        <path d="M44 60 L44 96 L90 96 L90 60"/>
        <rect x="57" y="68" width="20" height="16"/>
        <path d="M61 68 L61 62 Q67 54 73 62 L73 68"/>
      </g>
    </svg>
    <h3>Lorem Ipsum</h3>
    <p>Lorem ipsum dolor sit amet, consectetur adipiscing elit, sed do eiusmod tempor incididunt ut labore et dolore.</p>
  </div>

  <div class="abs service" style="left:785px">
    <svg width="134" height="134" viewBox="0 0 134 134">
      <circle cx="67" cy="67" r="63" fill="none" stroke="var(--blue)" stroke-width="3"/>
      <rect x="38" y="44" width="58" height="38" fill="var(--blue)"/>
      <path d="M60 82 L58 94 L76 94 L74 82 Z M50 96 L84 96" fill="var(--blue)" stroke="var(--blue)" stroke-width="3"/>
    </svg>
    <h3>Lorem Ipsum</h3>
    <p>Lorem ipsum dolor sit amet, consectetur adipiscing elit, sed do eiusmod tempor incididunt ut labore et dolore.</p>
  </div>
</section>

<section class="section team">
  <h2 class="abs title">Team</h2>
  <article class="abs member" style="left:124px">
    <div class="member-photo" role="img" aria-label="Portrait of team member by the waterfront" style="background:linear-gradient(180deg,#c8d3da 0%,#9fb0bb 35%,#5a4b42 60%,#1f2a44 100%)"></div>
    <h3>Corwin Hale</h3><div class="role">CEO</div>
    <p>Lorem ipsum dolor sit amet, consectetur adipiscing elit.</p>
  </article>
  <article class="abs member" style="left:450px">
    <div class="member-photo" role="img" aria-label="Portrait of team member in a suit" style="background:linear-gradient(180deg,#b9b3ad 0%,#a98d79 40%,#5d5a5c 70%,#2c2d33 100%)"></div>
    <h3>Milo Varden</h3><div class="role">Developer</div>
    <p>Lorem ipsum dolor sit amet, consectetur adipiscing elit.</p>
  </article>
  <article class="abs member" style="left:779px">
    <div class="member-photo" role="img" aria-label="Portrait of smiling team member" style="background:linear-gradient(180deg,#d4cfc8 0%,#a88a74 40%,#3f3c40 72%,#23242a 100%)"></div>
    <h3>Rowan Ashby</h3><div class="role">Developer</div>
    <p>Lorem ipsum dolor sit amet, consectetur adipiscing elit.</p>
  </article>
</section>

<footer class="section contact">
  <div class="contact-photo" role="img" aria-label="Glass office building at night"></div>
  <div class="footer-band"></div>
  <h2 class="abs title">Contact</h2>
  <div class="abs field" style="left:124px;top:145px;width:303px">Name</div>
  <div class="abs field" style="left:450px;top:145px;width:302px">Email</div>
  <div class="abs field" style="left:773px;top:145px;width:303px">Phone</div>
  <div class="abs field" style="left:124px;top:221px;width:952px;height:130px">Message</div>
  <div class="abs btn send">Send</div>
  <div class="abs footer-note">Brightfall Systems 2017</div>
</footer>

</body>
</html>
```